Standard Biz Card
Health Professionals
Please upload ai or eps of your logo
Kindly upload logo file in ai/eps format!
That contest is here: http://orders.markcraftplaza.example/contests/new-health-clinic-logo-biz-card
Sorry, there seem to be a misunderstandig as we thought this job was combined with the logo job. We do not have a logo yet, it is another contest going on at the moment.
Please upload the logo files

```html
<!DOCTYPE html>
<html lang="no">
<head>
<meta charset="utf-8">
<title>Visittkort – Erik Lindvik</title>
<link rel="stylesheet" href="https://fonts.googleapis.com/css2?family=Questrial&display=swap">
<style>
  :root {
    --page: #ffffff;
    --lime: #c1d72f;
    --lime-light: #d9e67f;
    --white: #ffffff;
    --frame: #8a8a8a;
    --font: "Questrial", "Century Gothic", sans-serif;
  }
  html, body {
    margin: 0;
    padding: 0;
    width: 1200px;
    height: 763px;
    overflow: hidden;
    background: var(--page);
    font-family: var(--font);
  }
  .card {
    position: absolute;
    left: 60px;
    top: 72px;
    width: 1082px;
    height: 624px;
    background: var(--lime);
    outline: 2px solid var(--frame);
    overflow: hidden;
  }
  .pattern-area {
    position: absolute;
  }
  .pattern-area--top {
    left: 631px;
    top: 0;
    width: 451px;
    height: 156px;
    background: linear-gradient(to bottom, var(--lime-light), var(--lime));
  }
  .pattern-area--bottom {
    left: 0;
    top: 492px;
    width: 432px;
    height: 132px;
    background: linear-gradient(to top, var(--lime-light), var(--lime));
  }
  .logo-box {
    position: absolute;
    left: 125px;
    top: 144px;
    width: 331px;
    height: 331px;
    background: var(--white);
    display: flex;
    align-items: center;
    justify-content: center;
  }
  .logo-box__label {
    color: var(--lime);
    font-size: 42px;
    letter-spacing: 0.5px;
  }
  .divider {
    position: absolute;
    left: 501px;
    top: 156px;
    width: 2px;
    height: 312px;
    background: var(--white);
  }
  .contact {
    position: absolute;
    left: 540px;
    top: 150px;
    color: var(--white);
  }
  .contact__name {
    margin: 0;
    font-size: 40px;
    font-weight: 400;
    line-height: 1.1;
  }
  .contact__title {
    margin: 6px 0 0;
    font-size: 24px;
  }
  .contact__details {
    margin: 62px 0 0;
    font-size: 25px;
    line-height: 34.5px;
    font-style: normal;
  }
</style>
</head>
<body>
  <div class="card">
    <div class="pattern-area pattern-area--top" role="img" aria-label="Dekorativt mønster i hvitt i øvre høyre hjørne"></div>
    <div class="pattern-area pattern-area--bottom" role="img" aria-label="Dekorativt mønster i hvitt i nedre venstre hjørne"></div>

    <div class="logo-box">
      <span class="logo-box__label">YOUR LOGO</span>
    </div>

    <div class="divider"></div>

    <div class="contact">
      <h1 class="contact__name">Erik Lindvik</h1>
      <p class="contact__title">Manuellterapeut</p>
      <address class="contact__details">
        Solbergveien 4, 1370 Nordvik<br>
        P: 00 00 00 00<br>
        F: 00 00 00 00<br>
        E: post@fjordmt.example<br>
        www.fjordmt.example
      </address>
    </div>
  </div>
</body>
</html>
```